Business Cards for new orthopaedic surgery practice

My husband and I are starting our own orthopaedic surgery practice. We are looking for a business card that is uniform, but one will have my name/title and the other will have his. You can just create one design with my name on it for now. But when I choose your design as the winning design I will ask that you add another copy with his name/title.

We are looking for classy, simple, elite all in one. We like dark blues/a little gold/yellow. Something that goes with our logo. We want our logo incorporated. Here is all the info you need:
Business name: RV Spine & Vitality Center
Location: 38915 North Bramble Ave
Marlow Heights, FL 33890
Phone: 954-218-4630
Fax: 954-571-2846
Email: info@myrvspine.example

Names: Lucinda Ferrow, M.D.
Board Certified Shoulder and Upper Limb Specialist

Emeka Dlunga, M.D.
Board Certified Hip & Knee Replacement/General Orthopaedic Surgeon

Can decide what you want to put on the back. Maybe a slogan:
Grounded in Care. Centered on You

I am just going to upload our logo. The only thing is if we select you as the winning design, the location, and phone numbers may change. We will need your help to update that once fully solidified.

Industry/Entity Type

Medical

Contact Information for Business Card

Colors
0054AA
0677BA
7BADD7
CADEEF
E8F1F8
0094D4
00A9DD
6FCCEA
C7EBF8
E9F6FB

Requirements
Must have
• class, appeal,
Should not have
• We want to air on the side of masculine if we are looking at masculine vs. feminine feel. But we still want it classy, sophisticated, and something we will love

```html
<!DOCTYPE html>
<html lang="en">
<head>
<meta charset="utf-8">
<title>RV Spine &amp; Vitality Center – Business Card</title>
<link href="https://fonts.googleapis.com/css2?family=Montserrat:wght@400;600;700&display=swap" rel="stylesheet">
<style>
  :root {
    --navy: #1b2a52;
    --gold: #c9a15a;
    --white: #ffffff;
    --stage: #e9ecf1;
    --ink: #1b2a52;
  }
  * { box-sizing: border-box; margin: 0; padding: 0; }
  html, body { width: 1200px; height: 931px; overflow: hidden; }
  body {
    background: var(--stage);
    font-family: 'Montserrat', sans-serif;
    position: relative;
  }
  .card {
    position: absolute;
    width: 560px;
    height: 320px;
    border-radius: 18px;
    overflow: hidden;
    box-shadow: 0 10px 28px rgba(20, 30, 60, 0.22);
  }
  .card--back { left: 60px; top: 60px; background: var(--navy); }
  .card--front { left: 580px; top: 551px; background: var(--white); }

  .brand-seal {
    position: absolute;
    display: flex;
    align-items: center;
    justify-content: center;
    text-align: center;
  }
  .brand-seal__ring {
    position: absolute;
    inset: 0;
    border: 2px solid var(--gold);
    border-radius: 50%;
  }
  .brand-seal__name {
    position: relative;
    font-weight: 600;
    letter-spacing: 0.12em;
    text-transform: uppercase;
    line-height: 1.5;
  }
  .card--back .brand-seal { left: 170px; top: 50px; width: 220px; height: 220px; }
  .card--back .brand-seal__name { color: var(--white); font-size: 17px; }
  .card--front .brand-seal { left: 36px; top: 34px; width: 180px; height: 180px; }
  .card--front .brand-seal__name { color: var(--navy); font-size: 13px; }

  .divider {
    position: absolute;
    left: 236px;
    top: 38px;
    width: 1px;
    height: 172px;
    background: var(--navy);
  }
  .details {
    position: absolute;
    left: 258px;
    top: 34px;
    color: var(--ink);
  }
  .details__name {
    font-size: 22px;
    font-weight: 700;
    color: var(--navy);
    letter-spacing: -0.01em;
    line-height: 1.2;
  }
  .details__name .credential { color: var(--gold); }
  .details__title {
    font-size: 11.5px;
    line-height: 1.3;
    margin-top: 3px;
  }
  .details__address {
    font-size: 11.5px;
    line-height: 1.3;
    margin-top: 14px;
  }
  .contact-list { list-style: none; margin-top: 8px; font-size: 11.5px; line-height: 1.6; }
  .contact-list li { display: flex; align-items: center; gap: 7px; }
  .contact-list svg { width: 11px; height: 11px; flex: none; }
  .icon-fill { fill: var(--gold); }

  .slogan-band {
    position: absolute;
    left: 0;
    right: 0;
    top: 234px;
    height: 44px;
    background: var(--navy);
    color: var(--white);
    font-weight: 700;
    font-size: 13px;
    display: flex;
    align-items: center;
    justify-content: center;
  }
  .base-stripe {
    position: absolute;
    left: 0;
    right: 0;
    top: 288px;
    height: 16px;
    background: var(--navy);
  }
</style>
</head>
<body>
  <section class="card card--back" aria-label="Card back">
    <div class="brand-seal">
      <span class="brand-seal__ring"></span>
      <span class="brand-seal__name">RV Spine &amp;<br>Vitality<br>Center</span>
    </div>
  </section>

  <section class="card card--front" aria-label="Card front">
    <div class="brand-seal">
      <span class="brand-seal__ring"></span>
      <span class="brand-seal__name">RV Spine &amp;<br>Vitality<br>Center</span>
    </div>

    <span class="divider"></span>

    <div class="details">
      <h1 class="details__name">Lucinda Ferrow, <span class="credential">M.D.</span></h1>
      <p class="details__title">Board Certified Shoulder and<br>Upper Limb Specialist</p>
      <p class="details__address">38915 North Bramble Ave<br>Marlow Heights, FL 33890</p>
      <ul class="contact-list">
        <li>
          <svg viewBox="0 0 12 12" aria-hidden="true"><path class="icon-fill" d="M2 1h2.5l1 2.5-1.3 1a6 6 0 0 0 3.3 3.3l1-1.3 2.5 1V10a1 1 0 0 1-1 1A9 9 0 0 1 1 2a1 1 0 0 1 1-1z"/></svg>
          954-218-4630
        </li>
        <li>
          <svg viewBox="0 0 12 12" aria-hidden="true"><rect class="icon-fill" x="3" y="1" width="6" height="3"/><rect class="icon-fill" x="1" y="4.5" width="10" height="4.5" rx="1"/><rect class="icon-fill" x="3" y="9.5" width="6" height="1.5"/></svg>
          954-571-2846
        </li>
        <li>
          <svg viewBox="0 0 12 12" aria-hidden="true"><rect class="icon-fill" x="1" y="2.5" width="10" height="7"/><path d="M1.5 3l4.5 3.5L10.5 3" fill="none" stroke="#fff" stroke-width="0.9"/></svg>
          info@myrvspine.example
        </li>
      </ul>
    </div>

    <div class="slogan-band">Grounded in Care. Centered on You</div>
    <span class="base-stripe"></span>
  </section>
</body>
</html>
```